Brightwell Wiring Needs A Logo Design

We need a logo for my new company based out of Sacramento, Ca called Brightwell Wiring. The name says it all, my electrical contracting business provides "Brightwell Craftsman Work" I'm open to any colors that pop and customers to say Wow. I would love to print my cards on metal.

Contact Information for Business Card

The card needs to have as follows
Name of company: Brightwell Wiring
My Name: Marco Delvane
Phone # 916-555-0147
CL# 4873920
Email: brightwellwiring@mailtorva.com
and a slogan that represent "BRIGHTWELL"

Requirements
Must have
• The card needs to have as follows
• Name of company: Brightwell Wiring
• My Name : Marco Delvane
• Phone # 916-555-0147
• CL# 4873920
• Email: brightwellwiring@mailtorva.com
• and a slogan that represent "BRIGHTWELL"
Nice to have
• popping colors
• electrical Arcing

```html
<!DOCTYPE html>
<html lang="en">
<head>
<meta charset="utf-8">
<title>Brightwell Wiring — Business Card</title>
<link rel="stylesheet" href="https://fonts.googleapis.com/css2?family=Montserrat:wght@600;700&family=Open+Sans:wght@400;600;700&display=swap">
<style>
  :root {
    --page-bg: #e9e6e1;
    --card-dark: #0b1322;
    --card-mid: #13294a;
    --glow-blue: #1c5fa8;
    --brand-blue: #1a7ac8;
    --text-white: #ffffff;
    --text-soft: #dfe7f1;
    --photo-tone: #2a6fb8;
  }
  * { box-sizing: border-box; margin: 0; padding: 0; }
  html, body { width: 1200px; height: 1000px; overflow: hidden; }
  body {
    position: relative;
    background: var(--page-bg);
    font-family: "Open Sans", Arial, sans-serif;
  }
  .card {
    position: absolute;
    left: 265px;
    width: 665px;
    height: 397px;
    overflow: hidden;
    color: var(--text-white);
  }
  .card--front {
    top: 73px;
    background: radial-gradient(ellipse 60% 65% at 55% 45%, var(--card-mid) 0%, var(--card-dark) 75%);
  }
  .card--back {
    top: 533px;
    background: radial-gradient(ellipse 75% 60% at 50% 95%, var(--glow-blue) 0%, var(--card-mid) 40%, var(--card-dark) 80%);
  }
  .brand {
    position: absolute;
    display: flex;
    flex-direction: column;
    align-items: center;
    font-family: "Montserrat", Arial, sans-serif;
    font-weight: 700;
    color: var(--brand-blue);
    text-transform: uppercase;
    line-height: 1.05;
    text-align: center;
  }
  .brand__mark {
    width: 24px; height: 24px;
    background: var(--brand-blue);
    margin-bottom: 16px;
  }
  .card--front .brand { left: 50px; top: 165px; width: 270px; font-size: 34px; }
  .card--back .brand { left: 0; right: 0; top: 62px; font-size: 44px; }
  .card--back .brand__mark { width: 30px; height: 30px; margin-bottom: 16px; }
  .divider {
    position: absolute;
    left: 333px; top: 130px;
    width: 2px; height: 145px;
    background: linear-gradient(to bottom, transparent, rgba(255,255,255,0.75), transparent);
  }
  .contact { position: absolute; left: 361px; top: 132px; }
  .contact__name {
    font-weight: 700; font-size: 20px; letter-spacing: 0.5px;
    text-transform: uppercase; margin-bottom: 26px;
  }
  .contact__name .surname { color: var(--brand-blue); }
  .contact__line {
    display: flex; align-items: center; gap: 7px;
    font-size: 15px; color: var(--text-soft); margin-bottom: 4px;
  }
  .contact__line svg { width: 14px; height: 14px; fill: var(--brand-blue); flex: none; }
  .contact__line--license { margin-bottom: 10px; }
  .arc-photo {
    position: absolute; left: 0; right: 0; top: 228px; height: 112px;
    background: radial-gradient(ellipse 60% 70% at 50% 55%, rgba(42,111,184,0.55) 0%, rgba(42,111,184,0.2) 55%, transparent 100%);
  }
  .slogan {
    position: absolute; left: 0; right: 0; top: 346px;
    text-align: center; font-weight: 600; font-size: 18px;
  }
</style>
</head>
<body>
  <section class="card card--front">
    <div class="brand">
      <span class="brand__mark"></span>
      <span>Brightwell</span>
      <span>Wiring</span>
    </div>
    <div class="divider"></div>
    <div class="contact">
      <p class="contact__name">Marco <span class="surname">Delvane</span></p>
      <p class="contact__line contact__line--license">CL# 4873920</p>
      <p class="contact__line">
        <svg viewBox="0 0 24 24"><path d="M6.6 10.8a15.1 15.1 0 0 0 6.6 6.6l2.2-2.2a1 1 0 0 1 1-.25 11.4 11.4 0 0 0 3.6.57 1 1 0 0 1 1 1V20a1 1 0 0 1-1 1A17 17 0 0 1 3 4a1 1 0 0 1 1-1h3.5a1 1 0 0 1 1 1c0 1.25.2 2.45.57 3.57a1 1 0 0 1-.25 1z"/></svg>
        916-555-0147
      </p>
      <p class="contact__line">
        <svg viewBox="0 0 24 24"><path d="M2 5h20v14H2z M2 5l10 8 10-8" fill="none" stroke="#1a7ac8" stroke-width="2"/><path d="M3 6l9 7 9-7v12H3z"/></svg>
        brightwellwiring@mailtorva.com
      </p>
    </div>
  </section>

  <section class="card card--back">
    <div class="brand">
      <span class="brand__mark"></span>
      <span>Brightwell</span>
      <span>Wiring</span>
    </div>
    <div class="arc-photo" role="img" aria-label="Photograph of two electrical cables with an electric arc between their exposed wires"></div>
    <p class="slogan">Brightwell Quality You Can See!</p>
  </section>
</body>
</html>
```